Need a Web Site Design - Fresh, Modern, and Visually Engaging Website Design

I’m looking to create a clean, modern, and visually appealing website that effectively represents our brand and services. The design should focus on user experience, intuitive navigation, and a professional aesthetic.

The Home page should set the tone for the entire site, featuring a sleek, modern layout with strong visual appeal.

Our Company Logo colors attached. The design can incorporate this color theme or use a unique palette that complements it.

Site Map:
We will begin with the following sections, with the potential to expand and add more services in the future:

Home: A welcoming and engaging introduction to our business, highlighting key services and industries we serve.
About Us: Share our story, mission, and values to connect with visitors.
Software Development: Showcase our expertise in developing innovative software solutions.
Industries We Serve: Provide detailed insights into the sectors we specialize in, including:
- Payroll Sector
- Education
- Transportation
- Home Care Services
Contact Us: Offer easy ways for clients to reach out, including forms and contact details.
Footer: Include essential links, social media handles, and company details.

Draft content for Services Page
Services
We specialize in delivering tailored solutions to meet your business needs. Our expertise spans Product Development, App Development, and Website Development.

1. Product Development
From concept to completion, we help you bring innovative products to life.
What We Offer:
• Custom Software Solutions: Scalable and secure software tailored to your business processes.
• Prototyping & MVP Development: Rapid prototyping and Minimum Viable Product creation to validate ideas.
• End-to-End Development: Comprehensive support from ideation to launch.
• Integration Services: Seamless integration of new products with your existing systems.

2. App Development
Build cutting-edge mobile and desktop applications to engage your audience and enhance operational efficiency.
What We Offer:
• Native & Cross-Platform Apps: Applications built for iOS, Android, and cross-platform frameworks.
• User-Centered Design: Apps designed with intuitive interfaces and smooth user experiences.
• Custom Features: Tailored functionality to meet your unique business needs.
• Maintenance & Updates: Continuous support to keep your app relevant and high-performing.

3. Website Development
Your website is the face of your business. We ensure it leaves a lasting impression.
What We Offer:
• Custom Website Design: Unique and responsive designs tailored to your brand identity.
• E-Commerce Development: Scalable and secure online stores to grow your business.
• CMS Integration: Easy-to-manage content systems like WordPress, Joomla, or custom CMS.
• SEO Optimization: Built-in search engine optimization for enhanced visibility.

Your Journey with Us
Our streamlined approach ensures that your project is handled with precision, creativity, and care. We partner with you at every step to create tailored solutions that transform your business.

Phase One: Discovery
We start by understanding your business inside and out, ensuring the foundation for our partnership is built on knowledge and alignment.
Assessment & Analysis
We dive deep into your business environment to uncover challenges, identify growth opportunities, and understand the economic factors driving your operations.
Process Evaluation
Our team analyzes your current workflows and processes, identifying inefficiencies and areas where improvements can enhance productivity and effectiveness.
Data-Driven Strategy
Using your organization’s technical and operational data, we create informed strategies that align with your goals and drive meaningful outcomes.

Phase Two: Estimate
We present a fully customized solution tailored to your needs, empowering you with the information required to make confident decisions.
Technology Plan & Roadmap
We design a detailed technology roadmap that includes the functionalities you need, the ideal tools and technologies, and a timeline for project completion.
Transition Planning
Our scope includes planning for a seamless transition, covering everything from system migration to user training and long-term usability.
Future Forecasting
Our solutions are built to grow with your business. We consider scalability, future technology trends, and your organization’s long-term needs to ensure lasting success.

Phase Three: Blueprint
Every successful project begins with a comprehensive plan. Our blueprints define every aspect of functionality, technology, and user experience, ensuring a smooth path forward.
Technology and Architecture
We develop a detailed framework outlining the infrastructure, external integrations, security measures, and scalability plans for the project.
Interactive Prototype
We create a clickable prototype that showcases the design, user interface, and functionality of the system, ensuring alignment with your vision.
Engineering & Testing Plan
Our strategy includes step-by-step engineering and rigorous testing for quality, security, and scalability throughout the development process.
Risk Management
We anticipate potential risks and outline mitigation strategies, reducing surprises and keeping the project on track.

Phase Four: Engineering
Our team of expert software engineers transforms the blueprint into a robust, scalable system tailored to your needs.
Full-Service Teams
We assemble a specialized team for your project, ensuring the skills and expertise align with your business goals and technical requirements.
Strategic Delivery
Our phased development approach delivers essential features first, reducing risks and enabling faster time-to-market.
Close Collaboration with Clients
We keep you informed and involved through every sprint, ensuring your vision is realized from the MVP to the final release.

Phase Five: Training & Support
We ensure a smooth integration of your new software, provide training for your team, and offer ongoing support to guarantee success.
Smooth Transition
We work with you to test new modules, retire outdated systems, and ensure a seamless rollout of the new solution.
Teamwide Training
Our team provides comprehensive training, gathers performance feedback, and optimizes the system for peak efficiency.
Long-Term Support
We continue to refine and improve the system post-launch, introducing enhancements to keep you ahead of the curve.

Our Projects
Explore our portfolio of completed projects, each showcasing our commitment to excellence and innovation.
(Provide a visually appealing UI design to display the project list, such as tiles or cards featuring images, project names, and a brief description.)

```html
<!DOCTYPE html>
<html lang="en">
<head>
<meta charset="utf-8">
<title>Nimbus Vale — R&amp;D Tax Relief &amp; Software</title>
<link href="https://fonts.googleapis.com/css2?family=Open+Sans:wght@400;600;700;800&display=swap" rel="stylesheet">
<style>
:root{
  --blue:#11a5e8;
  --navy:#0a3970;
  --orange:#f15a2b;
  --lime:#a8d13a;
  --green:#2e9a3a;
  --forest:#0b1d0f;
  --ink:#222;
  --grey:#555;
  --pale:#e9e9e9;
  --foot:#2b2b2b;
}
*{margin:0;padding:0;box-sizing:border-box}
html,body{width:1200px;height:4193px;overflow:hidden}
body{position:relative;font-family:"Open Sans",Arial,sans-serif;color:var(--ink);background:#fff;font-size:11px}
.abs{position:absolute}
.btn{position:absolute;background:var(--blue);color:#fff;font-weight:700;font-size:10.5px;text-transform:uppercase;display:flex;align-items:center;justify-content:center;border-radius:2px}
.h2{position:absolute;left:0;width:1200px;text-align:center;color:var(--blue);font-weight:700;font-size:26px;text-transform:uppercase}
.photo{position:absolute}
/* header */
.site-header{position:absolute;left:0;top:0;width:1200px;height:68px;background:#fff}
.brand{position:absolute;display:flex;align-items:center;gap:8px;color:var(--blue);font-weight:700;font-size:19px;text-transform:uppercase}
.brand i{width:22px;height:22px;background:var(--blue);border-radius:50%;display:block}
.nav{position:absolute;left:382px;top:26px;display:flex;gap:18px;font-size:11px}
.nav .active{color:var(--orange);text-decoration:underline}
/* hero */
.hero-title{position:absolute;left:156px;top:280px;color:#fff}
.hero-title b{display:block;font-size:36px;font-weight:800}
.hero-title span{display:block;font-size:23px;font-weight:400;margin-top:2px}
/* about */
.about-text{position:absolute;left:613px;top:740px;width:390px;font-size:10.5px;line-height:19px;color:var(--grey)}
.about-text h3{color:var(--blue);font-size:26px;font-weight:700;margin-bottom:12px}
.about-text p{margin-bottom:16px}
/* services */
.service{position:absolute;top:1360px;width:200px;color:#fff}
.service .icon{width:50px;height:44px;margin-bottom:24px}
.service h4{color:var(--lime);font-size:17px;line-height:19px;font-weight:700;text-transform:uppercase}
.service p{font-size:10.5px;line-height:16px;margin-top:6px;color:#e8eef6}
.service .arrow{width:30px;height:28px;margin-top:22px;background:#1e4f86;border-radius:2px;display:flex;align-items:center;justify-content:center}
.service .arrow.hot{background:var(--orange)}
/* industries */
.tile{position:absolute;width:388px;height:137px;overflow:hidden}
.tile .label{position:absolute;left:0;top:0;width:205px;height:137px;display:flex;align-items:center;justify-content:center;text-align:center;color:#fff;font-weight:700;font-size:18px;line-height:22px;text-transform:uppercase}
/* projects */
.card{position:absolute;left:200px;top:2589px;width:800px;height:374px;background:#fff}
.card h5{position:absolute;left:30px;top:42px;color:var(--green);font-size:19px;font-weight:700}
.card p{position:absolute;left:30px;width:255px;font-size:10px;line-height:15px;color:var(--ink)}
.card .year{position:absolute;left:30px;top:296px;color:var(--orange);font-size:22px;font-weight:800}
.card .done{position:absolute;left:30px;top:324px;font-size:9px;color:#999}
/* journey */
.tabs{position:absolute;left:200px;top:3346px;width:800px;border-top:1px solid #ddd}
.tab{position:absolute;top:20px}
.tab small{display:block;font-size:9.5px;color:var(--green)}
.tab b{display:block;font-size:16px;color:var(--green);font-weight:700;text-transform:uppercase}
.tab.on small,.tab.on b{color:var(--orange)}
.tab.on b{border-bottom:2px solid var(--orange);padding-bottom:2px}
.phase{position:absolute;left:200px;top:3432px;width:385px;font-size:10px;line-height:18px;color:var(--ink)}
.phase h6{font-size:10px;font-weight:700;margin-top:8px}
/* footer */
.footer-col{position:absolute;color:#ddd;font-size:10.5px;line-height:20px}
.footer-col h6{color:var(--blue);font-size:14px;font-weight:600;margin-bottom:12px}
.footer-col .cur{color:var(--orange);text-decoration:underline}
.copyright{position:absolute;left:0;top:4161px;width:1200px;height:32px;background:var(--blue);color:#fff;font-size:10px;line-height:32px;padding-left:156px}
.social{position:absolute;top:4170px;width:14px;height:14px;border-radius:50%;background:#fff;opacity:.9}
</style>
</head>
<body>

<header class="site-header">
  <div class="brand" style="left:156px;top:22px"><i></i>Nimbus Vale</div>
  <nav class="nav">
    <span class="active">Home</span><span>About Us</span><span>Claim Eligibility</span><span>Software Consultancy</span><span>Industries We Help</span><span>Contact Us</span>
  </nav>
  <div class="btn" style="left:914px;top:19px;width:130px;height:30px">Schedule a Call</div>
</header>

<!-- hero -->
<div class="photo" role="img" aria-label="Hands typing on a laptop with glowing code and web development graphics" style="left:0;top:68px;width:1200px;height:525px;background:linear-gradient(110deg,#020507 0%,#06202a 45%,#0c4a58 75%,#0a2a36 100%)"></div>
<svg class="abs" style="left:0;top:68px" width="1200" height="527" viewBox="0 0 1200 527">
  <polygon points="0,0 0,435 0,435" fill="none"/>
  <polygon points="0,435 100,525 1100,525 1200,435 1200,527 0,527" fill="#fff"/>
  <polyline points="0,435 100,521 1100,521 1200,435" fill="none" stroke="#11a5e8" stroke-width="6"/>
</svg>
<div class="hero-title"><b>HELPING BUSINESSES</b><span>CLAIM R&amp;D TAX RELIEF</span></div>

<!-- about -->
<svg class="abs" style="left:198px;top:690px" width="350" height="372">
  <polygon points="0,22 345,0 345,372 0,345" fill="#ececec"/>
</svg>
<div class="photo" role="img" aria-label="Illustration of a robot with a digital interface" style="left:208px;top:694px;width:338px;height:368px;background:linear-gradient(135deg,#1a2030,#2c3a55 60%,#101522);clip-path:polygon(0 5%,100% 0,100% 100%,0 94%)"></div>
<div class="about-text">
  <h3>ABOUT US</h3>
  <p>Nimbus Vale Ltd Has Been Set Up Specifically To Provide Guidance And Support To Small, Medium And Large Companies In Obtaining Tax Credit And Tax Benefits Under The Research And Development Tax Relief.</p>
  <p>We At Nimbus Vale Work With Some Of The Industry Experts In The Field Of Research And Development, Innovation, Tax Experts, Chartered Accountants And Lawyers Including Barristers To Provide A Tailor Made And Bespoke Guidance And In Support In Making Application To The Revenue Office For Research And Development Tax Relief.</p>
</div>
<div class="btn" style="left:613px;top:993px;width:80px;height:28px">Read More</div>

<!-- services band -->
<svg class="abs" style="left:0;top:1100px" width="1200" height="750">
  <polygon points="0,20 360,75 0,113" fill="#f15a2b"/>
  <polygon points="0,113 955,12 955,28 0,130" fill="#e6e6e6"/>
  <polygon points="0,130 1200,2 1200,613 0,745" fill="#0a3970"/>
</svg>
<div class="h2" style="top:1266px">Our Services</div>
<div class="service" style="left:199px">
  <svg class="icon" viewBox="0 0 50 44"><rect x="2" y="4" width="46" height="34" fill="none" stroke="#fff" stroke-width="2"/><line x1="2" y1="12" x2="48" y2="12" stroke="#fff" stroke-width="2"/><rect x="14" y="18" width="20" height="14" fill="none" stroke="#fff" stroke-width="2"/><rect x="20" y="18" width="8" height="6" fill="#a8d13a"/></svg>
  <h4>Product<br>Development</h4>
  <p>From concept to completion, we help you bring innovative products to life.</p>
  <div class="arrow"><svg width="12" height="12"><path d="M2 10 L10 2 M4 2 H10 V8" stroke="#9fb4cf" fill="none" stroke-width="1.4"/></svg></div>
</div>
<div class="service" style="left:496px">
  <svg class="icon" viewBox="0 0 50 44"><rect x="2" y="2" width="26" height="40" rx="3" fill="none" stroke="#fff" stroke-width="2"/><line x1="8" y1="14" x2="22" y2="14" stroke="#fff" stroke-width="2"/><line x1="8" y1="20" x2="22" y2="20" stroke="#fff" stroke-width="2"/><line x1="8" y1="26" x2="22" y2="26" stroke="#fff" stroke-width="2"/><rect x="24" y="6" width="20" height="12" fill="#a8d13a"/></svg>
  <h4>App<br>Development</h4>
  <p>Build cutting-edge mobile and desktop applications to engage your audience and enhance operational efficiency.</p>
  <div class="arrow"><svg width="12" height="12"><path d="M2 10 L10 2 M4 2 H10 V8" stroke="#9fb4cf" fill="none" stroke-width="1.4"/></svg></div>
</div>
<div class="service" style="left:792px">
  <svg class="icon" viewBox="0 0 50 44"><rect x="2" y="10" width="46" height="26" fill="none" stroke="#fff" stroke-width="2"/><line x1="18" y1="42" x2="32" y2="42" stroke="#fff" stroke-width="2"/><line x1="25" y1="36" x2="25" y2="42" stroke="#fff" stroke-width="2"/><rect x="14" y="2" width="22" height="14" fill="#a8d13a"/><path d="M21 6 L18 9 L21 12 M29 6 L32 9 L29 12" stroke="#0a3970" fill="none" stroke-width="1.5"/></svg>
  <h4>Website<br>Development</h4>
  <p>From concept to completion, we help you bring innovative products to life.</p>
  <div class="arrow hot"><svg width="14" height="12"><path d="M1 6 H12 M8 2 L12 6 L8 10" stroke="#fff" fill="none" stroke-width="1.4"/></svg></div>
</div>
<div class="btn" style="left:537px;top:1648px;width:126px;height:28px">Schedule a Call</div>

<!-- industries -->
<div class="h2" style="top:1882px">Industries We Serve</div>
<div class="tile" style="left:200px;top:1945px">
  <div class="photo" role="img" aria-label="Banknotes and wooden letter blocks spelling pay" style="left:0;top:0;width:388px;height:137px;background:linear-gradient(90deg,#6d5a44,#b79a72)"></div>
  <div class="label" style="background:var(--green);clip-path:polygon(0 0,100% 0,78% 100%,0 100%);width:225px;padding-right:40px">Payroll<br>Sector</div>
</div>
<div class="tile" style="left:612px;top:1945px">
  <div class="photo" role="img" aria-label="Hand writing in a notebook" style="left:0;top:0;width:388px;height:137px;background:linear-gradient(90deg,#c9b39a,#efe6dc)"></div>
  <div class="label" style="background:var(--orange);clip-path:polygon(0 0,100% 0,80% 100%,0 100%);width:230px;padding-right:40px">Education</div>
</div>
<div class="tile" style="left:200px;top:2108px">
  <div class="photo" role="img" aria-label="City highway interchange at night" style="left:0;top:0;width:388px;height:137px;background:linear-gradient(90deg,#2a3a66,#c08040)"></div>
  <div class="label" style="background:var(--blue);clip-path:polygon(0 0,100% 0,80% 100%,0 100%);width:240px;padding-right:30px">Transportation</div>
</div>
<div class="tile" style="left:612px;top:2108px">
  <div class="photo" role="img" aria-label="Carer attending to an elderly woman at home" style="left:0;top:0;width:388px;height:137px;background:linear-gradient(90deg,#7b8a9a,#d8d2c8)"></div>
  <div class="label" style="background:#8a3ff0;clip-path:polygon(0 0,100% 0,80% 100%,0 100%);width:230px;padding-right:40px">Home Care<br>Services</div>
</div>
<div class="btn" style="left:537px;top:2283px;width:126px;height:28px">Schedule a Call</div>

<!-- projects band -->
<svg class="abs" style="left:0;top:2365px" width="1200" height="835">
  <polygon points="0,20 360,78 0,98" fill="#2e9a3a"/>
  <polygon points="0,98 955,12 955,28 0,115" fill="#e6e6e6"/>
  <polygon points="0,115 1200,0 1200,712 0,834" fill="#0b1d0f"/>
</svg>
<div class="h2" style="top:2524px">Our Projects</div>
<div class="photo" role="img" aria-label="Faded preview of the previous project card" style="left:0;top:2589px;width:181px;height:374px;background:linear-gradient(90deg,#142418,#233528);opacity:.8"></div>
<div class="photo" role="img" aria-label="Faded preview of the next project card" style="left:1019px;top:2589px;width:181px;height:374px;background:linear-gradient(90deg,#2a352c,#1a261c);opacity:.8"></div>
<div class="card">
  <h5>PROJECT NAMES</h5>
  <p style="top:84px">Lorem Ipsum is simply dummy text of the printing and typesetting industry.</p>
  <p style="top:128px">Lorem Ipsum has been the industry's standard dummy text ever since the 1500s, when an unknown printer took a galley of type and scrambled it to make a type specimen book.</p>
  <div class="year">2024</div>
  <div class="done">Project done in</div>
  <div class="abs" style="left:130px;top:296px;width:30px;height:30px;background:var(--navy);border-radius:3px;display:flex;align-items:center;justify-content:center"><svg width="12" height="12"><path d="M2 10 L10 2 M4 2 H10 V8" stroke="#fff" fill="none" stroke-width="1.4"/></svg></div>
  <div class="abs" style="left:170px;top:305px;font-size:9px;color:#999">Visit Site</div>
  <div class="photo" role="img" aria-label="Man holding a folder with floating financial chart graphics" style="left:324px;top:0;width:476px;height:374px;background:linear-gradient(120deg,#2c4a66,#6d8eae 55%,#c7d3de)"></div>
</div>
<div class="btn" style="left:494px;top:3001px;width:136px;height:28px">View All Projects</div>
<div class="btn" style="left:643px;top:3001px;width:28px;height:28px"><svg width="14" height="12"><path d="M13 6 H2 M6 2 L2 6 L6 10" stroke="#fff" fill="none" stroke-width="1.4"/></svg></div>
<div class="btn" style="left:676px;top:3001px;width:28px;height:28px"><svg width="14" height="12"><path d="M1 6 H12 M8 2 L12 6 L8 10" stroke="#fff" fill="none" stroke-width="1.4"/></svg></div>

<!-- journey -->
<div class="h2" style="top:3235px">Your Journey With Us</div>
<p class="abs" style="left:290px;top:3287px;width:620px;text-align:center;font-size:10.5px;line-height:18px;color:var(--grey)">Our Streamlined Approach Ensures That Your Project Is Handled With Precision, Creativity, And Care. We Partner With You At Every Step To Create Tailored Solutions That Transform Your Business.</p>
<div class="tabs">
  <div class="tab on" style="left:0"><small>Phase One:</small><b>Discovery</b></div>
  <div class="tab" style="left:129px"><small>Phase Two:</small><b>Estimate</b></div>
  <div class="tab" style="left:248px"><small>Phase Three:</small><b>Blueprint</b></div>
  <div class="tab" style="left:377px"><small>Phase Four:</small><b>Engineering</b></div>
  <div class="tab" style="left:530px"><small>Phase Five:</small><b>Training &amp; Support</b></div>
</div>
<div class="phase">
  <p>We Start By Understanding Your Business Inside And Out, Ensuring The Foundation For Our Partnership Is Built On Knowledge And Alignment.</p>
  <h6>Assessment &amp; Analysis</h6>
  <p>We Dive Deep Into Your Business Environment To Uncover Challenges, Identify Growth Opportunities, And Understand The Economic Factors Driving Your Operations.</p>
  <h6>Process Evaluation</h6>
  <p>Our Team Analyzes Your Current Workflows And Processes, Identifying Inefficiencies And Areas Where Improvements Can Enhance Productivity And Effectiveness.</p>
  <h6>Data-Driven Strategy</h6>
  <p>Using Your Organization's Technical And Operational Data, We Create Informed Strategies That Align With Your Goals And Drive Meaningful Outcomes.</p>
</div>
<svg class="abs" style="left:636px;top:3428px" width="364" height="244"><polygon points="8,6 364,0 364,244 8,236" fill="#ececec"/></svg>
<div class="photo" role="img" aria-label="Climber walking along a snowy mountain ridge" style="left:644px;top:3436px;width:356px;height:230px;background:linear-gradient(160deg,#8fa8bf,#dfe7ee 60%,#f6f8fa);clip-path:polygon(0 3%,100% 0,100% 100%,0 97%)"></div>
<div class="btn" style="left:537px;top:3713px;width:126px;height:28px">Schedule a Call</div>

<!-- footer -->
<svg class="abs" style="left:0;top:3839px" width="1200" height="322">
  <polygon points="0,95 0,322 1200,322 1200,95 1100,0 100,0" fill="#2b2b2b"/>
  <polyline points="0,95 100,3 1100,3 1200,95" fill="none" stroke="#11a5e8" stroke-width="6"/>
</svg>
<div class="brand" style="left:156px;top:3900px"><i></i>Nimbus Vale</div>
<div class="footer-col" style="left:156px;top:3972px;width:200px">
  <h6>Contact Us</h6>
  <div>&#9990; 0200 555 0147</div>
  <div>&#9993; hello@nimbusvale.com</div>
  <div style="padding-left:14px;text-indent:-14px">&#9679; The Foundry Workspace, Suite 4, 12 Elm Lane, Ashford, Kent, TN0 1AB</div>
</div>
<div class="footer-col" style="left:404px;top:3972px;width:160px">
  <h6>Quick Links</h6>
  <div class="cur">Home</div><div>About Us</div><div>Claim Eligibility</div><div>Software Consultancy</div><div>Industries We Help</div><div>Contact Us</div>
</div>
<svg class="abs" style="left:622px;top:3903px" width="34" height="30"><rect x="2" y="6" width="30" height="22" fill="none" stroke="#f15a2b" stroke-width="2"/><path d="M2 6 L17 18 L32 6" fill="none" stroke="#f15a2b" stroke-width="2"/></svg>
<div class="abs" style="left:664px;top:3903px;color:var(--blue);font-size:11px;font-weight:600;line-height:14px">Subscribe to Our<br>Newsletter</div>
<div class="abs" style="left:790px;top:3900px;width:250px;height:34px;border:1px solid #555;color:#999;font-size:9.5px;line-height:32px;padding-left:12px">Enter Email</div>
<svg class="abs" style="left:1018px;top:3910px" width="16" height="14"><path d="M1 1 L15 7 L1 13 L4 7 Z" fill="#fff"/></svg>
<div class="photo" role="img" aria-label="Street map showing the office location" style="left:611px;top:3979px;width:431px;height:140px;background:linear-gradient(135deg,#eef0f2,#dfe3e7)"></div>
<div class="copyright">Copyright © 2024 Nimbus Vale, All rights reserved</div>
<div class="social" style="left:966px"></div>
<div class="social" style="left:993px"></div>
<div class="social" style="left:1020px;background:var(--orange)"></div>

</body>
</html>
```